Clean Energy Brand - Business Card and Letterhead Designs

Hi, everyone! We need a graphic designer who has experience working with the energy sector. We want help designing a perfect two-sided business card and letterhead for a clean energy company we've been assisting. We have a great new logo and all of the associated files.Our client is looking for a design that is "disruptive," "future-facing," "masculine," "bold," and "empowering." The colours of the logo are navy blue and orange and are meant to stand out. We'll need all ownership and copyright paperwork as well as first proofs in a 48-hour period.

Target Market(s)

Government; Non-Profits; Clean Energy Industry; Municipalities; North American Energy Sector

Industry/Entity Type

Power Generation

Requirements
Must have
• A matching business card and letterhead design
Should not have
• Must not be from a template

```html
<!DOCTYPE html>
<html lang="en">
<head>
<meta charset="utf-8">
<title>Northwind Clean Energy Letterhead</title>
<link href="https://fonts.googleapis.com/css2?family=Didact+Gothic&family=Poppins:wght@400;500&display=swap" rel="stylesheet">
<style>
  :root {
    --navy: #0f1a44;
    --orange: #ee5a24;
    --backdrop: #e3e3e3;
    --paper: #f1f1f1;
    --paper-shade: #dedede;
    --ink: #5a5a5a;
    --ink-dark: #4a4a4a;
    --white: #ffffff;
    --signature: #3a6bb0;
  }
  * { box-sizing: border-box; margin: 0; padding: 0; }
  html, body { width: 1023px; height: 1200px; overflow: hidden; }
  body { background: var(--backdrop); position: relative; font-family: "Didact Gothic", sans-serif; }

  .letterhead {
    position: absolute; left: 88px; top: 8px;
    width: 846px; height: 1185px;
    background: linear-gradient(90deg, var(--paper) 0%, var(--paper-shade) 100%);
    box-shadow: 0 6px 30px rgba(0,0,0,0.12);
  }

  .brand { position: absolute; left: 82px; top: 84px; width: 206px; text-align: center; }
  .brand-dot { display: block; width: 44px; height: 44px; border-radius: 50%; background: var(--orange); margin: 0 auto 12px; }
  .brand-name { font-family: "Poppins", sans-serif; font-weight: 500; font-size: 30px; line-height: 34px; color: var(--navy); letter-spacing: -0.5px; }
  .brand-tagline { font-family: "Poppins", sans-serif; font-weight: 500; font-size: 11.5px; letter-spacing: 3.6px; color: var(--navy); margin-top: 2px; }

  .contact-panel {
    position: absolute; left: 568px; top: 74px; width: 278px; height: 124px;
    background: var(--navy); color: var(--white);
    font-family: "Poppins", sans-serif; font-size: 12.5px; line-height: 15.5px;
    text-align: right; padding: 12px 70px 0 0;
  }
  .contact-company { font-weight: 500; }
  .contact-lines { margin-top: 5px; }
  .contact-line { display: flex; justify-content: flex-end; align-items: center; gap: 6px; height: 17px; margin-right: -18px; }
  .contact-line svg { width: 11px; height: 11px; fill: var(--white); }

  .letter { position: absolute; left: 82px; top: 308px; width: 694px; color: var(--ink); }
  .salutation { font-size: 21px; color: var(--ink-dark); margin-bottom: 40px; }
  .letter p.body { font-size: 12.8px; line-height: 18px; margin-bottom: 18px; text-align: justify; }
  .closing { font-size: 12.8px; margin-top: 36px; }
  .signature {
    margin-top: 42px; width: 145px; height: 70px; border-radius: 4px;
    background: linear-gradient(90deg, rgba(58,107,176,0.18), rgba(58,107,176,0.08));
  }
</style>
</head>
<body>
  <main class="letterhead">
    <header>
      <div class="brand">
        <span class="brand-dot"></span>
        <div class="brand-name">northwind</div>
        <div class="brand-tagline">CLEAN ENERGY</div>
      </div>

      <address class="contact-panel" style="font-style: normal;">
        <div class="contact-company">Northwind Clean Energy</div>
        <div>4120 Ridgeway Drive</div>
        <div>Fairbanks, Alaska 99701</div>
        <div class="contact-lines">
          <div class="contact-line">555-014-2738
            <svg viewBox="0 0 24 24" aria-hidden="true"><path d="M6.6 10.8a15 15 0 0 0 6.6 6.6l2.2-2.2a1 1 0 0 1 1-.25 11.4 11.4 0 0 0 3.6.57 1 1 0 0 1 1 1V20a1 1 0 0 1-1 1A17 17 0 0 1 3 4a1 1 0 0 1 1-1h3.5a1 1 0 0 1 1 1c0 1.25.2 2.45.57 3.57a1 1 0 0 1-.25 1z"/></svg>
          </div>
          <div class="contact-line">hello@northwindenergy.com
            <svg viewBox="0 0 24 24" aria-hidden="true"><path d="M2 5h20v14H2z M2 5l10 8 10-8" stroke="#0f1a44" stroke-width="1.5"/></svg>
          </div>
          <div class="contact-line">www.northwindenergy.com
            <svg viewBox="0 0 24 24" aria-hidden="true"><circle cx="12" cy="12" r="10"/><path d="M7 8c2 0 3 1 3 3s2 2 2 4-1 3-1 4M15 5c-1 2 0 3 2 3s3 2 3 3" stroke="#0f1a44" stroke-width="1.6" fill="none"/></svg>
          </div>
        </div>
      </address>
    </header>

    <section class="letter">
      <p class="salutation">Dear Mr. Harlow,</p>
      <p class="body">Lorem ipsum dolor sit amet, consectetur adipiscing elit. Donec orci purus, luctus vitae dignissim eu, iaculis sed purus. Vivamus faucibus, ipsum nec aliquet viverra, leo mauris condimentum ligula, sit amet sagittis enim ligula quis arcu. Nam egestas tortor id nisi porttitor mattis. In tortor ante, ultricies in suscipit a, tempus non massa. Vivamus et auctor mi. Fusce vel massa nulla. Phasellus nec eros mauris, et scelerisque orci.</p>
      <p class="body">Donec malesuada orci vitae nulla accumsan porta a id massa. Quisque accumsan iaculis magna sit amet fringilla. Maecenas consequat, magna eget tincidunt semper, odio nibh rutrum mi, id feugiat ante nisi eu risus. Vestibulum nunc orci, rhoncus a placerat in, ultricies in mi. Cras mattis varius eros, vel fringilla nisi suscipit eget. Quisque scelerisque sagittis nulla at porttitor.</p>
      <p class="body">Sed id augue vitae urna euismod commodo aliquet a quam. Pellentesque arcu velit, cursus et malesuada ut, consequat et diam. Nullam erat sem, rhoncus id ullamcorper vitae, rhoncus et arcu. In ultricies ultricies nulla, ut rutrum nisi iaculis at. Donec eu magna a metus ornare faucibus. Fusce aliquet faucibus ultricies. Morbi semper, est id tincidunt gravida, sem arcu adipiscing lacus, ac bibendum nulla leo eu purus. Quisque nec diam sed risus consectetur a ccumsan quis quis nibh. Vestibulum id purus lorem.</p>
      <p class="body">It is a long established fact that a reader will be distracted by the readable content of a page when looking at its layout. The point of using Lorem Ipsum is that it has a more-or-less normal distribution of letters, as opposed to using 'Content here, content here', making it look like readable English. Many desktop publishing packages</p>
      <p class="closing">Sincerely,</p>
      <div class="signature" role="img" aria-label="Handwritten signature of Daniel Harlow"></div>
    </section>
  </main>
</body>
</html>
```